Prestige Car Bodyshop Business Card

We are a car bodyshop based in the UK. Our customer base is mainly prestige high-value vehicles. I am looking for a classy and stylish business card design for my staff to give out to customers, with their direct email and phone number, as well as our main email and phone number with address details

I am also looking to have a general business card design with just our main company address and contact details, but also have a space to add a manufacturer approval logo (i.e Velmora, Orek, Tovalo etc... logo) in the corner somewhere.

I do not particularly want any outlines or pictures of cars on the card, I would just like a quality high-end look.

Please feel free to get in touch if you have any questions or queries?

Many Thanks

Malcolm

Target Market(s)

Prestige vehicle owners

Industry/Entity Type

Automotive

Contact Information for Business Card

I am looking for a classy and stylish business card design for my staff to give out to customers, with their direct email and phone number, as well as our main email and phone number with address details

Font styles to use
Sans Serif

Colors

Designer to choose colors to be used in the design.

Requirements
Nice to have
• I do not particularly want any outlines or pictures of cars on the card, I would just like a quality high-end look.

```html
<!DOCTYPE html>
<html lang="en">
<head>
<meta charset="utf-8">
<title>Branwell Accident Repair Centre – Business Card</title>
<link href="https://fonts.googleapis.com/css2?family=Open+Sans:wght@400;600;700&display=swap" rel="stylesheet">
<style>
  :root {
    --page-bg: #e9ebee;
    --card-bg: #ffffff;
    --navy: #1f3a6e;
    --navy-deep: #14295a;
    --orange: #e0661c;
    --ink: #1c1f2a;
    --rule: #8a8f99;
  }
  html, body {
    margin: 0;
    padding: 0;
    width: 1200px;
    height: 970px;
    overflow: hidden;
    background: var(--page-bg);
    font-family: "Open Sans", Arial, sans-serif;
  }
  .card {
    position: absolute;
    left: 100px;
    top: 207px;
    width: 1000px;
    height: 556px;
    background: var(--card-bg);
    border-radius: 26px;
    overflow: hidden;
    box-shadow: 0 10px 30px rgba(20, 30, 60, 0.15);
  }
  .card-base {
    position: absolute;
    left: 0;
    right: 0;
    bottom: 0;
    height: 62px;
    background: var(--navy-deep);
    border-top: 5px solid var(--orange);
  }
  .brand {
    position: absolute;
    left: 48px;
    top: 45px;
    display: flex;
    align-items: center;
    gap: 23px;
  }
  .brand-dot {
    width: 165px;
    height: 165px;
    border-radius: 50%;
    background: var(--navy);
  }
  .brand-name {
    color: var(--navy-deep);
    font-weight: 400;
  }
  .brand-name .first {
    display: block;
    font-size: 54px;
    line-height: 1;
    padding-bottom: 8px;
    border-bottom: 2px solid var(--navy-deep);
    width: 306px;
  }
  .brand-name .second {
    display: block;
    font-size: 19.5px;
    letter-spacing: 0.6px;
    margin-top: 6px;
  }
  .divider {
    position: absolute;
    left: 48px;
    top: 287px;
    width: 680px;
    height: 2px;
    background: var(--rule);
  }
  .person {
    position: absolute;
    right: 48px;
    top: 240px;
    text-align: right;
  }
  .person-name {
    color: var(--orange);
    font-weight: 700;
    font-size: 29px;
    letter-spacing: 0.5px;
    margin: 0;
    line-height: 1.1;
  }
  .person-role {
    color: var(--ink);
    font-size: 22px;
    margin: 0;
    line-height: 1.3;
  }
  .contacts {
    position: absolute;
    left: 48px;
    top: 306px;
    list-style: none;
    margin: 0;
    padding: 0;
    color: var(--ink);
    font-size: 22px;
  }
  .contacts li {
    display: flex;
    align-items: center;
    gap: 12px;
    height: 34.5px;
  }
  .contacts svg { width: 20px; height: 20px; fill: var(--ink); flex: none; }
  .address {
    position: absolute;
    right: 48px;
    top: 356px;
    text-align: right;
    color: var(--ink);
    font-size: 22px;
    line-height: 33px;
    font-style: normal;
  }
</style>
</head>
<body>
  <section class="card">
    <div class="card-base"></div>

    <div class="brand">
      <div class="brand-dot"></div>
      <div class="brand-name">
        <span class="first">BRANWELL</span>
        <span class="second">ACCIDENT REPAIR CENTRE</span>
      </div>
    </div>

    <div class="divider"></div>

    <div class="person">
      <h1 class="person-name">ELOWEN MARSH</h1>
      <p class="person-role">Managing Director</p>
    </div>

    <ul class="contacts">
      <li>
        <svg viewBox="0 0 20 20"><path d="M6 1h8a1 1 0 0 1 1 1v16a1 1 0 0 1-1 1H6a1 1 0 0 1-1-1V2a1 1 0 0 1 1-1zm1 3v7h6V4zm1 9v2h1v-2zm2.5 0v2h1v-2zm2.5 0v2h1v-2z"/></svg>
        <span>+ 000 000 0000</span>
      </li>
      <li>
        <svg viewBox="0 0 20 20"><path d="M2 7c0-3 4-4 8-4s8 1 8 4v1h-4V6H6v2H2zm3 2h10l3 8H2zm5 2a2.5 2.5 0 1 0 0 5 2.5 2.5 0 0 0 0-5z"/></svg>
        <span>+ 000 000 0000</span>
      </li>
      <li>
        <svg viewBox="0 0 20 20"><path d="M1 4h18v1l-9 6-9-6zm0 3 9 6 9-6v9H1z"/></svg>
        <span>elowen@branwellrepair.com</span>
      </li>
      <li>
        <svg viewBox="0 0 20 20"><path d="M10 1a9 9 0 1 0 0 18 9 9 0 0 0 0-18zm0 2c1 0 2 2 2.4 5H7.6C8 5 9 3 10 3zM3.1 8h2.5a14 14 0 0 0 0 4H3.1a7 7 0 0 1 0-4zm4.5 4a12 12 0 0 1 0-4h4.8a12 12 0 0 1 0 4zm6.8 0a14 14 0 0 0 0-4h2.5a7 7 0 0 1 0 4zM10 17c-1 0-2-2-2.4-3h4.8c-.4 1-1.4 3-2.4 3z"/></svg>
        <span>www.branwellrepair.com</span>
      </li>
    </ul>

    <address class="address">
      Level 18, 4 Aldren Tower<br>
      Brackton, 20, North Vale
    </address>
  </section>
</body>
</html>
```